Rack Card Design for an Ayurvedic Beauty Product Project

Hello, I need to have rack cards. The rack cards would be about 3 products we are showcasing at an event. I am a cosmetic company. I have a logo and basic design ideas. I have attached some product images and info. By no means am I a designer so please excuse my messy AI files. Please feel free to design this as feminine as you like. :)

Target Market(s)

Beauty industry, organic, holistic, ayurveda

Industry/Entity Type

Cosmetic

```html
<!DOCTYPE html>
<html lang="en">
<head>
<meta charset="utf-8">
<title>Amber Bloom Rack Cards</title>
<link href="https://fonts.googleapis.com/css2?family=Montserrat:wght@300;400;600;700&display=swap" rel="stylesheet">
<style>
  :root {
    --plum: #8a2a5f;
    --plum-deep: #6e1f4a;
    --blush: #fbe9f0;
    --blush-soft: #fff6f9;
    --gold: #c9a56a;
    --gold-light: #efdcb5;
    --ink: #3a2a33;
    --muted: #6d5a64;
    --white: #ffffff;
    --stage: #eeeae6;
  }
  * { box-sizing: border-box; margin: 0; padding: 0; }
  html, body { width: 882px; height: 1200px; overflow: hidden; }
  body {
    background: var(--stage);
    font-family: "Montserrat", sans-serif;
    position: relative;
  }
  .rack-card {
    position: absolute;
    top: 148px;
    width: 400px;
    height: 904px;
    background: linear-gradient(180deg, var(--blush-soft), var(--blush) 60%, var(--blush-soft));
    overflow: hidden;
    box-shadow: 0 6px 18px rgba(0,0,0,.18);
  }
  .rack-card--front { left: 26px; }
  .rack-card--list { left: 456px; }

  .card-header { position: absolute; top: 0; left: 0; width: 400px; height: 220px; }
  .card-header svg { position: absolute; inset: 0; }
  .brand {
    position: absolute; top: 20px; left: 0; width: 400px;
    display: flex; flex-direction: column; align-items: center; gap: 12px;
  }
  .brand-dot { width: 84px; height: 84px; border-radius: 50%; background: var(--white); }
  .brand-name { color: var(--white); font-weight: 600; font-size: 17px; letter-spacing: 1px; }

  .hero-photo {
    position: absolute; top: 150px; left: 0; width: 400px; height: 463px;
    background: radial-gradient(ellipse at 50% 45%, #f1d6c8 0%, #f7e4e6 45%, var(--blush) 80%);
  }
  .product-shot {
    position: absolute; border-radius: 6px;
    background: linear-gradient(180deg, #9b3a70 0%, var(--plum-deep) 78%, var(--gold) 78%, var(--gold-light) 100%);
  }
  .product-shot--hero { left: 300px; top: 480px; width: 64px; height: 165px; }

  .intro {
    position: absolute; top: 613px; left: 0; width: 400px; height: 245px;
    background: var(--plum); color: var(--white);
    padding: 36px 30px 0; text-align: center;
    font-size: 12.2px; font-weight: 300; line-height: 1.24;
  }
  .intro p + p { margin-top: 13px; }

  .card-footer {
    position: absolute; bottom: 0; left: 0; width: 400px; height: 46px;
    background: linear-gradient(90deg, var(--gold-light), var(--gold) 20%, #f6ead0 50%, var(--gold) 80%, var(--gold-light));
    display: flex; align-items: center; justify-content: center; gap: 7px;
    color: #1d1d1d; font-size: 20px; font-weight: 400;
  }
  .card-footer b { font-weight: 600; }

  .list-title {
    position: absolute; top: 204px; left: 24px; width: 352px; height: 42px;
    border-radius: 21px; background: var(--plum);
    border: 2px solid var(--gold-light);
    color: var(--white); font-weight: 600; font-size: 20px; letter-spacing: .5px;
    display: flex; align-items: center; justify-content: center;
  }
  .product { position: absolute; left: 30px; width: 350px; }
  .product-name {
    position: absolute; left: 112px; top: 0; width: 240px;
    color: var(--plum); font-weight: 700; font-size: 14.5px; line-height: 1.2;
  }
  .product-text {
    position: absolute; left: 112px; top: 46px; width: 210px;
    color: var(--muted); font-size: 12.5px; line-height: 1.2;
  }
  .product--toner { top: 280px; }
  .product--cream { top: 466px; }
  .product--serum { top: 664px; }
  .product .product-shot { left: 10px; top: 0; width: 58px; height: 146px; }
  .product--cream .jar-lid { position: absolute; left: 10px; top: -6px; width: 58px; height: 58px; border-radius: 50%; background: radial-gradient(circle, #9b3a70, var(--plum-deep)); border: 2px solid var(--gold); }
  .product--cream .jar-body { position: absolute; left: 12px; top: 60px; width: 54px; height: 66px; border-radius: 8px; background: linear-gradient(180deg, var(--gold-light), #f4eef0 25%, #e7d9de); }
</style>
</head>
<body>

<section class="rack-card rack-card--front">
  <div class="hero-photo" role="img" aria-label="Portrait photo of a woman with hands framing her face, soft blush background"></div>
  <div class="product-shot product-shot--hero" role="img" aria-label="Plum and gold product tube"></div>
  <header class="card-header">
    <svg width="400" height="220" viewBox="0 0 400 220">
      <path d="M0 0 H400 V130 C300 200 120 210 0 150 Z" fill="#8a2a5f"/>
      <path d="M0 150 C120 210 300 200 400 130 L400 142 C300 214 120 222 0 160 Z" fill="#c9a56a"/>
    </svg>
    <div class="brand">
      <span class="brand-dot"></span>
      <span class="brand-name">AMBER BLOOM</span>
    </div>
  </header>
  <div class="intro">
    <p>Amber Bloom curates organic infused products where holistic skin care meets a luxurious experience. Each ingredient is carefully selected; providing Ayurvedic herbs, rich minerals &amp; elements. Stimulating hydration and anti-oxidants to lift, firm and illuminate your skin.</p>
    <p>We believe in connecting with your inner mantra, stimulating higher vibrations, self-esteem, positive mind and soul. As a brand we work with our experts/suppliers of Ayurveda to ensure that our products meet the quality, wholesome healing that you need.</p>
  </div>
  <footer class="card-footer">
    <svg width="20" height="20" viewBox="0 0 20 20" fill="none" stroke="#1d1d1d" stroke-width="1.4"><circle cx="10" cy="10" r="8"/><ellipse cx="10" cy="10" rx="3.5" ry="8"/><path d="M2 10 H18 M4 5.5 H16 M4 14.5 H16"/></svg>
    <span>www.<b>amberbloom</b>.com</span>
  </footer>
</section>

<section class="rack-card rack-card--list">
  <header class="card-header">
    <svg width="400" height="220" viewBox="0 0 400 220">
      <path d="M0 0 H400 V94 C300 200 100 200 0 56 Z" fill="#8a2a5f"/>
      <path d="M0 56 C100 200 300 200 400 94 L400 106 C300 213 100 213 0 67 Z" fill="#c9a56a"/>
    </svg>
    <div class="brand">
      <span class="brand-dot"></span>
      <span class="brand-name">AMBER BLOOM</span>
    </div>
  </header>
  <div class="list-title">AMBER BLOOM PRODUCT LIST</div>

  <article class="product product--toner">
    <div class="product-shot" role="img" aria-label="Breast toner tube"></div>
    <h3 class="product-name">AMBER BLOOM FIRMING AND LIFTING BREAST TONER</h3>
    <p class="product-text">Using all natural Ayurvedic herbs, our breast toner, prepares the area for maximum absorption, giving you the best results and the most invigorating treatment</p>
  </article>

  <article class="product product--cream">
    <div class="jar-body" role="img" aria-label="Breast cream jar"></div>
    <div class="jar-lid"></div>
    <h3 class="product-name">AMBER BLOOM FIRMING AND LIFTING BREAST CREAM</h3>
    <p class="product-text">Using all natural Ayurvedic herbs, our breast cream helps enhance, tighten, and lift your breast</p>
  </article>

  <article class="product product--serum">
    <div class="product-shot" role="img" aria-label="Breast serum tube"></div>
    <h3 class="product-name">AMBER BLOOM FIRMING AND TONING BREAST SERUM</h3>
    <p class="product-text">Using all natural Ayurvedic herbs, and a touch of 24k gold, our serum enhances the experience and quality of results when partnered with the Amber Bloom Firming and Lifting Breast Cream providing an all-day boosting experience</p>
  </article>

  <footer class="card-footer">
    <svg width="20" height="20" viewBox="0 0 20 20" fill="none" stroke="#1d1d1d" stroke-width="1.4"><circle cx="10" cy="10" r="8"/><ellipse cx="10" cy="10" rx="3.5" ry="8"/><path d="M2 10 H18 M4 5.5 H16 M4 14.5 H16"/></svg>
    <span>www.<b>amberbloom</b>.com</span>
  </footer>
</section>

</body>
</html>
```